Petal Sprite - web design for my new flower atelier

I would like to ask for design proposal for my newly established flower atelier. My brand name is Petal Sprite and I focus on realisation of events and flower projects (any kind) for physical as well as legel persons. I don’t operate as a standard flowershop. I would like to have 5 key parts - 1/Landing pg/welcome, 2/About me, 3/Gallery, 4/References, 5/Contact details. I would like the web design to reflect the way I am/ I do the things, ie, be slightly different, do non-tradiotional arrangements, my passion for flowers, gentle& fregile style, love for minimalism and details in the arrangements. I attach couple of photos of what I do so that you can better understand my style . You can see more on IG mirka_petal_sprite or FB Petal Sprite. I was wondering maybe one of the first 2 photos could be part of the landing pg. Or another idea is to have a design similar to this one https://thistlebloomstudio.example, ie to choose 3-5photos which are being animated like here. However, I am open to discuss any ideas and look forward for all the proposals.

Target Market(s)

physical as well as legal persons - weddings, celebrations, business events, projects for hotels, beaty salons, restaurants and others.. actually any kind of flower project

Industry/Entity Type

flowers

Number of Pages Required

1 page

Font styles to use
Other font styles liked:
• the font which matches the logo font style

Requirements
Must have
• to reflect the way I am as described above, I prefer more simple way of design, with the attention to a detail, I prefer pastel colours

```html
<!DOCTYPE html>
<html lang="en">
<head>
<meta charset="utf-8">
<title>Petal Sprite – Flower Atelier</title>
<link rel="stylesheet" href="https://fonts.googleapis.com/css2?family=Quicksand:wght@400;500;600&family=Allison&display=swap">
<style>
:root{
  --brown:#806340;
  --taupe:#c5b9aa;
  --cream:#e7ddd1;
  --sage:#a3bda8;
  --mint:#cbdfd0;
  --mint-line:#b5ccb7;
  --ink:#3f3a33;
  --muted:#9a9187;
  --canvas:#f8f8f8;
  --white:#ffffff;
  --sans:'Quicksand', Arial, sans-serif;
  --script:'Allison', cursive;
}
*{margin:0;padding:0;box-sizing:border-box}
html,body{width:1200px;height:3698px;overflow:hidden;background:var(--canvas);font-family:var(--sans);color:var(--ink)}
.page{position:absolute;left:150px;top:28px;width:900px;height:3642px;background:var(--white);box-shadow:0 0 18px rgba(0,0,0,.05);overflow:hidden}
.abs{position:absolute}
.top-band{left:0;top:0;width:900px;height:560px;background:var(--taupe)}
.topbar{left:57px;top:24px;width:787px;display:flex;justify-content:space-between;font-size:9px;color:var(--white)}
.topbar .social{display:flex;gap:6px}
.dot{width:8px;height:8px;border-radius:50%;background:currentColor;display:inline-block}
.hero{left:57px;top:57px;width:787px;height:561px;background:linear-gradient(180deg,#f2f2f2 0%,#e6e6e6 55%,#d9d9d9 100%)}
.hero-flowers{left:110px;top:150px;width:560px;height:340px;border-radius:50%;background:radial-gradient(ellipse at center,#b7783a 0%,#8a7a3e 40%,rgba(120,110,70,.35) 65%,rgba(230,230,230,0) 75%)}
.nav{top:118px;font-size:10px;color:var(--muted)}
.logo{left:350px;top:70px;width:200px;text-align:center}
.logo-circle{width:46px;height:46px;border:1px solid var(--brown);border-radius:50%;margin:0 auto 8px}
.logo-name{font-size:15px;color:var(--brown);font-weight:500;letter-spacing:.5px}
.hero-title{left:219px;top:295px;width:465px;height:89px;background:var(--brown);color:var(--white);font-family:var(--script);font-size:54px;display:flex;align-items:center;justify-content:center;white-space:nowrap}
.sprig{width:40px;height:40px;border:1px solid var(--taupe);border-radius:50%;left:430px}
.stem{width:1px;background:var(--taupe);left:450px}
.card{border:none}
.card::after{content:"";position:absolute;inset:10px;border:1px solid rgba(255,255,255,.7)}
.card-mint{background:var(--mint)}
.card-cream{background:var(--cream)}
.card-cream::after{border-color:rgba(128,99,64,.25)}
.eyebrow{font-size:9px;letter-spacing:2px;text-transform:uppercase;color:var(--muted);text-align:center}
.script{font-family:var(--script);color:var(--brown);font-weight:400;line-height:1}
.card-body{position:absolute;left:0;width:100%;text-align:center}
.lead{font-size:10px;color:var(--ink)}
.photo{background:#ccc}
.frame{background:var(--white);box-shadow:0 0 6px rgba(0,0,0,.08);padding:8px}
.frame .photo{width:100%;height:100%}
.body-text{font-size:9.5px;line-height:18px;color:var(--ink)}
.link{font-size:9px;color:var(--muted)}
.btn{background:var(--sage);color:var(--white);font-size:8px;letter-spacing:1px;display:flex;align-items:center;justify-content:center}
.service{width:110px;text-align:center;font-size:8px;color:var(--muted);text-transform:uppercase}
.service-icon{width:48px;height:48px;border:1px solid var(--mint-line);border-radius:50%;margin:0 auto 10px}
.bottom-band{left:0;top:3335px;width:900px;height:307px;background:#f7f7f7}
.input{background:var(--white);font-size:8px;color:var(--muted);padding-left:12px;display:flex;align-items:center}
.btn-brown{background:var(--brown);color:var(--white);font-size:8px;letter-spacing:.5px;display:flex;align-items:center;justify-content:center;font-weight:600}
.foot-title{font-size:11px;color:var(--muted);margin-bottom:16px}
.foot-text{font-size:8.5px;line-height:15px;color:var(--brown)}
.foot-social{display:flex;gap:7px;color:var(--brown);margin-bottom:8px}
</style>
</head>
<body>
<main class="page">
  <div class="abs top-band"></div>
  <div class="abs topbar"><span>hello@petalsprite.example &nbsp;|&nbsp; +1 555 010 2040</span><span class="social"><span class="dot"></span><span class="dot"></span><span class="dot"></span></span></div>

  <section class="abs hero">
    <div class="abs hero-flowers" role="img" aria-label="Wild autumn flower arrangement with orange blooms, leaves and bare twigs"></div>
  </section>
  <nav>
    <span class="abs nav" style="left:122px">Home</span>
    <span class="abs nav" style="left:190px">About Me</span>
    <span class="abs nav" style="left:675px">Gallery</span>
    <span class="abs nav" style="left:750px">Contact</span>
  </nav>
  <div class="abs logo"><div class="logo-circle"></div><div class="logo-name">Petal Sprite</div></div>
  <h1 class="abs hero-title">Petal Sprite – As in Fairytale</h1>

  <div class="abs sprig" style="top:683px"></div>
  <div class="abs stem" style="top:723px;height:45px"></div>
  <section class="abs card card-mint" style="left:122px;top:768px;width:655px;height:300px">
    <p class="card-body eyebrow" style="top:38px">Welcome to Petal Sprite</p>
    <h2 class="card-body script" style="top:78px;font-size:50px;line-height:54px">Flowers Make Everyone's<br>Day Brighter &amp; Fun</h2>
    <p class="card-body lead" style="top:206px">Liquenean sollicitudin, lorem quis bibendum auct ornisi elit quot ipsum</p>
  </section>

  <div class="abs photo" style="left:0;top:990px;width:257px;height:344px;background:linear-gradient(160deg,#d4d4d4,#b8b8b8)" role="img" aria-label="Dried cotton stems in a slim beige vase"></div>
  <p class="abs script" style="left:471px;top:1150px;font-size:50px">Let's Dream Together!</p>

  <div class="abs photo" style="left:580px;top:1279px;width:320px;height:403px;background:linear-gradient(180deg,#e8e8e8,#cfcfcf)" role="img" aria-label="Tall branches with yellow flowers in a dark green glass vase"></div>
  <div class="abs frame" style="left:464px;top:1326px;width:315px;height:388px">
    <div class="photo" style="background:linear-gradient(150deg,#8c8274,#6b6a5e 50%,#b49a7c)" role="img" aria-label="Florist in a knitted scarf holding a wrapped bouquet"></div>
  </div>
  <h2 class="abs script" style="left:124px;top:1418px;font-size:52px">About Me</h2>
  <p class="abs body-text" style="left:124px;top:1486px;width:205px">Lorem ipsum dolor sit amet congit. Proin quat do quis ereingolus. Liquenean sollicitudin, lorem quis bibendum auct ornisi elit consequat ipsum, nec sagittis sem nibh id elit. vulputate cursus a sit amet Mauri s. Mei possim sit amet Maur lorem quis adec bibendum auct ornisi</p>
  <span class="abs link" style="left:124px;top:1612px">Learn More &rarr;</span>

  <div class="abs sprig" style="top:1781px"></div>
  <div class="abs stem" style="top:1821px;height:43px"></div>
  <section class="abs card card-cream" style="left:122px;top:1864px;width:657px;height:302px">
    <p class="card-body eyebrow" style="top:40px">Let's Connect</p>
    <h2 class="card-body script" style="top:86px;font-size:50px">Got Any Flower Project?</h2>
    <a class="abs btn" style="left:281px;top:173px;width:95px;height:38px">LET'S TALK</a>
  </section>
  <div class="abs frame" style="left:646px;top:2090px;width:254px;height:334px">
    <div class="photo" style="background:linear-gradient(180deg,#eceae6,#a35a3a 45%,#6e5a40 80%,#8a6a4a)" role="img" aria-label="Loose bouquet of orange roses and dried grasses on a wooden stand"></div>
  </div>
  <h2 class="abs script" style="left:124px;top:2200px;font-size:50px;line-height:48px">Petal Sprite &amp;<br>Event Arrangement</h2>
  <div class="abs service" style="left:103px;top:2369px"><div class="service-icon"></div>Wedding Event</div>
  <div class="abs service" style="left:196px;top:2369px"><div class="service-icon"></div>Business Event</div>
  <div class="abs service" style="left:300px;top:2369px"><div class="service-icon"></div>Any Flower Project</div>

  <div class="abs frame" style="left:-8px;top:2540px;width:126px;height:272px">
    <div class="photo" style="background:linear-gradient(160deg,#a0593a,#d8b3a3 50%,#4b4038)" role="img" aria-label="Protea arrangement by a brick wall"></div>
  </div>
  <div class="abs frame" style="left:143px;top:2540px;width:195px;height:272px">
    <div class="photo" style="background:linear-gradient(180deg,#5a5a5a,#bfc3c5 60%,#3e4246)" role="img" aria-label="Single flower in a glass vase on a table"></div>
  </div>
  <div class="abs frame" style="left:365px;top:2540px;width:201px;height:272px">
    <div class="photo" style="background:linear-gradient(180deg,#f1efe9,#d6b850 55%,#a9c26c 85%)" role="img" aria-label="Yellow and orange flowers in a green glass vase"></div>
  </div>
  <p class="abs eyebrow" style="left:606px;top:2640px;text-align:left">Recent Work</p>
  <h2 class="abs script" style="left:606px;top:2665px;font-size:50px">My Gallery</h2>

  <h2 class="abs script" style="left:0;top:2915px;width:900px;text-align:center;font-size:50px;line-height:58px">Need a Planning For Your Event?<br>Contact Me!</h2>
  <p class="abs lead" style="left:0;top:3040px;width:900px;text-align:center">Lorem ipsum dolor sit amet congit. Liquenean sollicitudin, lorem quis bibendum auct ornisi elit</p>

  <div class="abs bottom-band"></div>
  <section class="abs card card-mint" style="left:122px;top:3148px;width:657px;height:293px">
    <h2 class="card-body script" style="top:92px;font-size:50px">Subscribe to Newsletter</h2>
    <div class="abs input" style="left:150px;top:150px;width:262px;height:38px">Your Email Address</div>
    <div class="abs btn-brown" style="left:412px;top:150px;width:93px;height:38px">SUBSCRIBE</div>
  </section>

  <footer>
    <div class="abs" style="left:124px;top:3500px;width:200px">
      <p class="foot-title">About Me</p>
      <p class="foot-text">Lorem ipsum dolor sit amet<br>consectetur adipiscing elit, sed</p>
    </div>
    <div class="abs" style="left:412px;top:3500px;width:200px">
      <p class="foot-title">Contact Me</p>
      <p class="foot-text">&#9993; studio@petalsprite.example<br>&#9742; +1 555 010 2040</p>
    </div>
    <div class="abs" style="left:669px;top:3500px;width:200px">
      <p class="foot-title">Connect With Me</p>
      <div class="foot-social"><span class="dot"></span><span class="dot"></span><span class="dot"></span></div>
      <p class="foot-text" style="font-size:7px">2022 &copy; Petal Sprite</p>
    </div>
  </footer>
</main>
</body>
</html>
```